Sportdrink für Fussballer
Zielgruppe
WER WIR SIND?
Wir sind ein junges Label, das es sich zur Aufgabe macht, ambitionierte Fussballspieler aus dem Amateurbereich in Training & Spiel mit qualitativ hochwertiger Sportnahrung auszustatten.
Unsere Produkte richten sich an Sportler, die immer alles geben und mit unserer Unterstützung zu wahren Legenden auf dem Platz werden möchten.
Besucht auch gerne unseren Snapwall Channel: torheldwerk
ZIELGRUPPE?
- Ambitionierte Amateurfussballspieler und -spielerinnen
- Alter: 16 - 30
- Fitnessaffin / Gesundheits & Ernährungsbewusst
- Trendy / hipster
- Bewusstsein für Mode, Ästhetik, Nachhaltigkeit
Aufgabenstellung
Liebe Designer!
Für unser Produkt - ein isotonisches Getränkepulver - benötigen wir eure Expertise bei der Gestaltung eines ansprechenden Etiketts.
Unser Getränkepulver wird in Dosen mit einer Höhe von 12,5 cm und einem Durchmesser von 9 cm angeboten (siehe Anhang für Beispieldose).
Die exakten Maße zur Gestaltung des Etiketts können der beigefügten Druckstandsskizze entnommen werden ( 4 farbig, Chromolux 80g / qm).
1) Generelle Anmerkungen zum gewünschten Design:
- Unser Produkt richtet sich ausschließlich an die Zielgruppe "Fussballer"
- Das Etikett sollte stilistisch auf jeden Fall in die Richtung "handmade / handcrafted" gehen (siehe Beispiele)
- Das Etikett sollte möglichst clean sein und nur vereinzelte Farbelemente enthalten (idealerweise weißer oder schwarzer Hintergrund)
- Das Logo sollte das Kernelement des Etiketts sein (siehe Fox Hall)
- Zur Besseren Visualisierung sollte jedem 2D Entwurf auch ein 3D Entwurf beigefügt werden
2) Elemente auf der Vorderseite
- Logo (großflächige Darstellung) im "used-look" (abgesplittert, zerkratzt, etc…)
- Produktname: "Isotonisches Sportgetränk"
- Logos für folgende Produkteigenschaften:
o Echtes Fruchtpulver
o Keine künstlichen Zusatzstoffe
o Hergestellt in Deutschland
- Box oder Farbband für Geschmacksrichtung: "Zitrone/Limette" ( Sollte sich gut dafür eignen auch andere Geschmacksrichtungen darstellen zu können)
- Platzhalter für Grammangabe (200 bzw. 400 Gramm)
3) Elemente auf der Rückseite
- Text:
Die letzten Minuten laufen. Dein Wille ist ungebrochen aber jeder Sprint bringt deine Oberschenkel zum brennen. Du willst den Sieg, deine Muskeln nur noch die Eistonne. Laut einer Studie des KSV sind deine Energiereserven je nach Spielposition nach 60 bis 70 Minuten vollständig erschöpft.
Die Folgen:
x Unnötige Fehlpässe
x Fehlende Spritzigkeit

```html
<!DOCTYPE html>
<html lang="de">
<head>
<meta charset="utf-8">
<title>Torheldwerk – Isotonischer Sportdrink Etikett</title>
<link href="https://fonts.googleapis.com/css2?family=Roboto+Condensed:wght@400;700&family=Black+Ops+One&display=swap" rel="stylesheet">
<style>
  :root {
    --page: #f4f4f4;
    --label: #000000;
    --lime: #95c11f;
    --white: #ffffff;
    --grey: #d9d9d9;
  }
  * { margin: 0; padding: 0; box-sizing: border-box; }
  html, body { width: 914px; height: 1200px; overflow: hidden; background: var(--page); }
  body { position: relative; font-family: "Roboto Condensed", sans-serif; }

  .label {
    position: absolute; left: 17px; top: 415px;
    width: 880px; height: 369px;
    background: var(--label); color: var(--white);
    overflow: hidden;
  }
  .label__seam {
    position: absolute; left: 0; top: 0; width: 8px; height: 100%;
    background: repeating-linear-gradient(135deg, #1c1c1c 0 2px, transparent 2px 6px);
  }

  /* Brand block */
  .brand {
    position: absolute; left: 96px; top: 92px; width: 240px;
    text-align: center;
  }
  .brand__name {
    font-family: "Roboto Condensed", sans-serif; font-weight: 700;
    font-size: 33px; letter-spacing: 1px; color: var(--white);
    line-height: 1;
  }
  .brand__est {
    display: flex; align-items: center; justify-content: center; gap: 5px;
    margin-top: 6px; font-size: 9px; font-weight: 700; color: var(--white);
  }
  .brand__est::before, .brand__est::after {
    content: ""; width: 22px; height: 1px; background: var(--white);
  }
  .brand__product {
    margin-top: 12px; font-family: "Black Ops One", sans-serif;
    font-size: 13px; line-height: 1.15; letter-spacing: 1px; color: var(--lime);
  }

  /* Property hexagons */
  .feature {
    position: absolute; left: 420px; width: 76px; height: 66px;
  }
  .feature svg { position: absolute; inset: 0; }
  .feature__text {
    position: absolute; inset: 0; display: flex; align-items: center; justify-content: center;
    text-align: center; font-size: 8.5px; line-height: 1.3;
  }
  .feature--fruit { top: 27px; }
  .feature--pure { top: 124px; }
  .feature--made { top: 222px; }

  /* Back copy */
  .copy {
    position: absolute; left: 555px; top: 27px; width: 268px;
    font-size: 5.3px; line-height: 7.7px; text-align: justify;
  }
  .copy p { margin-bottom: 6px; }
  .copy .accent { color: var(--lime); }
  .consequences { display: flex; justify-content: space-between; margin-bottom: 6px; }
  .consequences span + span::before {
    content: ""; display: inline-block; width: 4px; height: 4px; border-radius: 50%;
    background: var(--lime); margin-right: 6px; vertical-align: middle;
  }

  .facts { display: grid; grid-template-columns: 44px 1fr; margin-bottom: 6px; }
  .facts__title { color: var(--lime); padding-top: 8px; }
  .facts table { width: 100%; border-collapse: collapse; }
  .facts th { color: var(--lime); font-weight: 400; text-align: left; padding-left: 9px; height: 8px; }
  .facts td { height: 8px; padding-left: 8px; border-right: 1px solid var(--label); }
  .facts tr.is-marked td { background: var(--lime); }
  .facts col.name { width: 41%; }
  .facts col.portion { width: 32%; }

  /* Flavour band */
  .flavour {
    position: absolute; left: 0; top: 320px; width: 100%; height: 21px;
    background: var(--lime);
  }
  .flavour__name {
    position: absolute; left: 176px; top: 2px; width: 112px; text-align: center;
    font-family: "Black Ops One", sans-serif; font-size: 11px; letter-spacing: 1px; color: var(--white);
  }
  .flavour__social {
    position: absolute; left: 555px; top: 6px; font-size: 5.3px; color: var(--white);
  }
  .flavour__icons { position: absolute; left: 713px; top: 4px; display: flex; gap: 4px; }
  .flavour__icons span { width: 13px; height: 13px; border-radius: 2px; background: var(--label); }
  .flavour__web { position: absolute; right: 57px; top: 6px; font-size: 5.3px; color: var(--white); }

  .weight {
    position: absolute; right: 57px; top: 348px;
    font-family: "Black Ops One", sans-serif; font-size: 11px; color: var(--white);
  }

  .distributor {
    position: absolute; left: 849px; top: 306px; transform-origin: left top;
    transform: rotate(-90deg); white-space: nowrap; font-size: 5.3px; color: var(--white);
  }
</style>
</head>
<body>
  <section class="label">
    <div class="label__seam"></div>

    <div class="brand">
      <div class="brand__name">TORHELDWERK</div>
      <div class="brand__est">Est. 2017</div>
      <div class="brand__product">ISOTONISCHER<br>SPORTDRINK</div>
    </div>

    <div class="feature feature--fruit">
      <svg viewBox="0 0 76 66"><polygon points="19,1 57,1 75,33 57,65 19,65 1,33" fill="none" stroke="var(--lime)" stroke-width="1"/><polygon points="21,4 55,4 72,33 55,62 21,62 4,33" fill="none" stroke="var(--lime)" stroke-width="0.7"/></svg>
      <div class="feature__text">Echtes<br>Fruchtpulver</div>
    </div>
    <div class="feature feature--pure">
      <svg viewBox="0 0 76 66"><polygon points="19,1 57,1 75,33 57,65 19,65 1,33" fill="none" stroke="var(--lime)" stroke-width="1"/><polygon points="21,4 55,4 72,33 55,62 21,62 4,33" fill="none" stroke="var(--lime)" stroke-width="0.7"/></svg>
      <div class="feature__text">Ohne<br>künstliche<br>Zusatzstoffe</div>
    </div>
    <div class="feature feature--made">
      <svg viewBox="0 0 76 66"><polygon points="19,1 57,1 75,33 57,65 19,65 1,33" fill="none" stroke="var(--lime)" stroke-width="1"/><polygon points="21,4 55,4 72,33 55,62 21,62 4,33" fill="none" stroke="var(--lime)" stroke-width="0.7"/></svg>
      <div class="feature__text">Hergestellt in<br>Deutschland</div>
    </div>

    <div class="copy">
      <p>Die letzten Minuten laufen. Dein Wille ist ungebrochen aber jeder Sprint bringt deine Oberschenkel zum brennen. Du willst den Sieg, deine Muskeln nur noch die Eistonne. Laut einer Studie des KSV sind deine Energiereserven je nach Spielposition nach 60 bis 70 Minuten vollständig erschöpft. Die Folgen:</p>
      <div class="consequences">
        <span>Unnötige Fehlpässe</span><span>Schwaches Zweikampfverhalten</span><span>Fehlende Spritzigkeit</span><span>Mangelnde Konzentration</span>
      </div>
      <p>Um deine Speicher schnell wieder aufzuladen brauchst du Energie! Nachdem uns die üblichen Sportgetränke zu süß, bunt und künstlich waren, haben wir es uns zur Aufgabe gemacht, eine natürliche Alternative zu entwickeln. Dabei verzichten wir bewusst auf künstliche Farb-, Aroma- und Konservierungsstoffe und bedienen uns stattdessen nur an natürlichen Inhaltsstoffen. Als besonderes Highlight verarbeiten wir für unser Sportgetränk echte Früchte, die deinen Geschmacksknospen ein Grinsen ins Gesicht zaubern.</p>
      <p><span class="accent">Zubereitung- &amp; Verzehrempfehlung</span> Die Zubereitung ist easy: Je nach Vorliebe 24 g Pulver in 450 bis 550 ml Wasser geben, kräftig schütteln, fertig! Für eine optimale Flüssigkeits- und Energieversorgung in Training und Spiel empfehlen wir bereits beim Aufwärmen ca. 150 - 300 ml zu trinken. Während der Belastung sollte dann im Abstand von 15 Minuten ca. 150 ml getrunken werden.</p>

      <div class="facts">
        <div class="facts__title">Nährwerte</div>
        <table>
          <colgroup><col class="name"><col class="portion"><col></colgroup>
          <tr><th></th><th>pro Portion (24g)</th><th>pro 100g</th></tr>
          <tr class="is-marked"><td>Energie</td><td>336 kJ / 80 kcal</td><td>1334 kJ / 320 kcal</td></tr>
          <tr><td>Fett</td><td>0 g</td><td>0 g</td></tr>
          <tr class="is-marked"><td>davon gesättigte Fettsäuren</td><td>0 g</td><td>0 g</td></tr>
          <tr><td>Kohlenhydrate</td><td>21 g</td><td>84 g</td></tr>
          <tr class="is-marked"><td>davon Zucker</td><td>20 g</td><td>80 g</td></tr>
          <tr><td>Eiweiss</td><td>0 g</td><td>0 g</td></tr>
          <tr class="is-marked"><td>Salz</td><td>900 mg</td><td>3600 mg</td></tr>
        </table>
      </div>
      <div class="facts">
        <div class="facts__title">Inhaltsstoffe</div>
        <table>
          <colgroup><col class="name"><col class="portion"><col></colgroup>
          <tr><th></th><th>pro Portion (24g)</th><th>in % NR?</th></tr>
          <tr class="is-marked"><td>Natrium</td><td>360 mg</td><td>15 %</td></tr>
          <tr><td>Vitamin C</td><td>28 mg</td><td>35 %</td></tr>
        </table>
      </div>
      <p><span class="accent">Zutatenliste</span> Rohrzucker, Traubenzucker, Natriumcitrat, Zitronensäure, Magnesiumlactat, Calciumcitrat, Zitronensaft, Limettensaft, Kaliumcitrat, Ascorbinsäure (Vitamin C)</p>
      <p>Außerhalb der Reichweite von Kindern aufbewahren. Die empfohlene tägliche Verzehrmenge darf nicht überschritten werden. Nahrungsergänzungsmittel sollten nicht als Ersatz für eine ausgewogene und abwechslungsreiche Ernährung dienen. Kühl, trocken und dunkel aufbewahren.</p>
    </div>

    <div class="distributor">Vertrieb durch Feliks Brauner Sport Commerce, Lindenallee 14, 50667 Brückstadt</div>

    <div class="flavour">
      <div class="flavour__name">Zitrone-Limette</div>
      <div class="flavour__social">STAY TUNED und folge uns auf Snapwall, Friendbook und im Web</div>
      <div class="flavour__icons"><span></span><span></span></div>
      <div class="flavour__web">www.torheldwerk.drink</div>
    </div>

    <div class="weight">200g ℮</div>
  </section>
</body>
</html>
```